Label Brelomo Beer Can for Exhibition promo not consumer sale

label for exhibtion promotional craft beer. I publish international trade techology magazines and after 13 years are unveiling a redesign for the magazines- new logo, new paper etc. The beer is for drinking and I am sure will get a bit of social promo within the trade.

Exhibtion Attendees, clients, readers

• Ultimately, it is 205mm wide by 87mm high. The guides in the file show the correct split for an aesthetically pleasing design that will get all the important info/branding on the front, and the legal stuff like the barcode and allergens on the back. Once done ,we will also likely need the source files too so that the correct barcode and ingredients can be dropped in
• We prefer a dorvalik can style (document 1)

```html
<!DOCTYPE html>
<html lang="en">
<head>
<meta charset="utf-8">
<title>Brelomo Hoppy Lager Ale – Can Label</title>
<link rel="stylesheet" href="https://fonts.googleapis.com/css2?family=Kanit:wght@800&family=Oswald:wght@500;600&family=Libre+Caslon+Text:wght@700&display=swap">
<style>
  :root {
    --page-bg: #f2f2f2;
    --label-black: #1b1b1d;
    --label-red: #e30613;
    --label-white: #ffffff;
    --icon-dark: #1b1b1d;
  }
  html, body {
    margin: 0;
    padding: 0;
    width: 1200px;
    height: 930px;
    overflow: hidden;
    background: var(--page-bg);
  }
  .canvas {
    position: relative;
    width: 1200px;
    height: 930px;
  }
  .can-label {
    position: absolute;
    left: 290px;
    top: 86px;
    width: 620px;
    height: 758px;
    display: block;
  }
  .arch-title {
    font-family: "Kanit", "Arial Black", sans-serif;
    font-weight: 800;
    font-size: 62px;
    fill: var(--label-white);
  }
  .region-line {
    font-family: "Kanit", "Arial Black", sans-serif;
    font-weight: 800;
    font-size: 58px;
    fill: var(--label-white);
  }
  .brand-name {
    font-family: "Libre Caslon Text", Georgia, serif;
    font-weight: 700;
    font-size: 104px;
    fill: var(--label-white);
  }
  .frame-caption {
    font-family: "Oswald", "Arial Narrow", sans-serif;
    font-weight: 600;
    font-size: 22px;
  }
  .frame-caption--white { fill: var(--label-white); }
  .frame-caption--red { fill: var(--label-red); }
  .redesign-line {
    font-family: "Oswald", "Arial Narrow", sans-serif;
    font-weight: 600;
    font-size: 28px;
    fill: var(--label-black);
  }
  .est-year {
    font-family: "Oswald", "Arial Narrow", sans-serif;
    font-weight: 600;
    font-size: 22px;
    fill: var(--label-white);
  }
  .trade-mark {
    font-family: "Kanit", "Arial Black", sans-serif;
    font-weight: 800;
    font-size: 15px;
    letter-spacing: 2px;
    fill: var(--label-red);
  }
</style>
</head>
<body>
<main class="canvas">
  <svg class="can-label" viewBox="0 0 628 768" xmlns="http://www.w3.org/2000/svg" aria-label="Brelomo Hoppy Lager Ale can label">
    <defs>
      <path id="title-arc" d="M59,390 A258,258 0 0 1 575,390"/>
      <path id="region-arc" d="M104,470 A213,213 0 0 0 530,470"/>
    </defs>

    <!-- label ground -->
    <rect class="label-ground" x="0" y="0" width="628" height="768" fill="var(--label-black)"/>

    <!-- framing lines -->
    <rect class="frame-outer" x="32" y="27" width="564" height="711" fill="none" stroke="var(--label-white)" stroke-width="6"/>
    <rect class="frame-inner" x="45" y="38" width="538" height="690" fill="none" stroke="var(--label-white)" stroke-width="3"/>

    <!-- red upper panel -->
    <rect class="panel-red" x="52" y="44" width="524" height="280" fill="var(--label-red)"/>

    <!-- outer thin arc -->
    <path class="title-arc-line" d="M54,390 A300,300 0 0 1 574,330" fill="none" stroke="var(--label-white)" stroke-width="3"/>

    <!-- arched title -->
    <text class="arch-title">
      <textPath href="#title-arc" startOffset="50%" text-anchor="middle" textLength="480" lengthAdjust="spacingAndGlyphs">HOPPY LAGER ALE</textPath>
    </text>

    <!-- upper dome -->
    <path class="dome-upper" d="M160,330 A157,157 0 0 1 474,330 L474,300 L474,320 Z" fill="var(--label-white)"/>
    <rect x="160" y="326" width="314" height="20" fill="var(--label-white)"/>
    <path class="dome-upper-rule" d="M172,340 A145,145 0 0 1 462,340" fill="none" stroke="var(--label-black)" stroke-width="6"/>

    <!-- brand mark area -->
    <circle class="brand-dot" cx="317" cy="232" r="36" fill="var(--label-red)"/>
    <text class="trade-mark" x="236" y="277" text-anchor="middle">TRADE</text>
    <text class="trade-mark" x="397" y="277" text-anchor="middle">MARK</text>

    <!-- lower bowl -->
    <path class="bowl-lower" d="M162,440 L162,470 A155,155 0 0 0 472,470 L472,440 Z" fill="var(--label-white)"/>
    <path class="bowl-lower-rule" d="M174,450 L174,470 A143,143 0 0 0 460,470 L460,450" fill="none" stroke="var(--label-black)" stroke-width="6"/>

    <!-- ribbon banner -->
    <path class="ribbon-outer" d="M40,298 L150,288 L478,288 L588,298 L588,332 L622,372 L588,412 L588,446 L478,456 L150,456 L40,446 L40,412 L6,372 L40,332 Z" fill="var(--label-white)"/>
    <path class="ribbon-inner" d="M46,304 L150,295 L478,295 L582,304 L582,336 L613,372 L582,408 L582,440 L478,449 L150,449 L46,440 L46,408 L15,372 L46,336 Z" fill="var(--label-black)"/>
    <rect class="ribbon-plate" x="30" y="310" width="568" height="124" fill="var(--label-black)" stroke="var(--label-white)" stroke-width="4"/>
    <text class="brand-name" x="314" y="406" text-anchor="middle">Brelomo</text>

    <!-- lower panel details -->
    <text class="redesign-line" x="317" y="482" text-anchor="middle">REDESIGN 2019</text>
    <text class="est-year" x="106" y="498" text-anchor="middle">EST.</text>
    <text class="est-year" x="524" y="501" text-anchor="middle">2005</text>
    <rect class="toast-icon" x="252" y="496" width="130" height="120" rx="6" fill="var(--icon-dark)" role="img" aria-label="Icon of two clinking beer mugs with foam droplets"/>

    <text class="region-line">
      <textPath href="#region-arc" startOffset="50%" text-anchor="middle" textLength="540" lengthAdjust="spacingAndGlyphs">APAC EMEA RUSSIA</textPath>
    </text>

    <!-- frame captions -->
    <rect x="200" y="14" width="228" height="28" fill="var(--label-black)"/>
    <text class="frame-caption frame-caption--white" x="319" y="37" text-anchor="middle">ORIGINAL CONTENT</text>
    <rect x="128" y="722" width="384" height="30" fill="var(--label-black)"/>
    <text class="frame-caption frame-caption--red" x="320" y="746" text-anchor="middle">BREWED WITH NATURAL INGREDIENTS</text>
  </svg>
</main>
</body>
</html>
```